Meridian Cataract Surgery and Cosmetic Eyelid Surgery

We need Three page website design (home page and interior page template with two looks) with accompanying CSS code. 1. Home page, 2. General Eye-Care page, 3. Cosmetic Eyelid Surgery. #2 an #3 would be only slightly different. See below.

The site being redesigned is http://www.bright-lumen.com.

The content will remain consistent with the current site.

Additional graphics will be included, especially a number of "Before and after" photos of patients for the various procedures.

You can see competitive sites here: http://www.findoraq.com/search?q=cosmetic+eyelid+surgury+santa+rosa&ie=utf-8&oe=utf-8&aq=t&client=browser-b&rlz=1R1TTPP_en___US384

The client likes http://www.view-pmr.com, which has a serious look he likes (not necessarily the colors or design). Avoid too many "happy loving couples" and pretty women, on the main page or cataract/general eye-care pages. They are, however, good on the cosmetic pages.

When patients look at the *cosmetic surgery* pages, they can see the pretty women/couples. For *eye surgery* (which is what this is all about) they should see an attractive, active OLDER couple(s) on cataract surgery and refractive surgery pages.

In the US, premium IOL (Intraocular lens - a clear plastic lens that is implanted in the eye; usually done when the natural lens has been removed in a cataract operation) cataract surgery, cosmetic and refractive surgery are not fully paid for by insurance, so patients can afford to pay for it themselves and are more well-off than the normal market.
Updates

Do not use the graphics or look and feel of the current site.  We are looking for a NEW design, not a remix of the old elements.

The new logo is at http://www.artmarketo.com/file.aspx?fileLocation=claritonvisionlogo0.jpg

 
Do NOT use the old logo.  If your submitted design uses the old logo, please fix it and delete the one with the old logo.

Sorry for not making this clearer when we started.

Normal 0 false false false EN-US X-NONE X-NONE I want to see a home page that gives equal billing to general eyecare and cosmetic and RECONSTRUCTIVE eyelid surgery.   General eyecare should be listed first.  This should have the correct Practice name and Logo:   Meridian Sightcare and Cosmetic Eyelid Surgery Center.  The home page should be inviting to both old and young, men and women.  The General eyecare page should have similar appeal.  Cosmetic Page should be decidedly more feminine.  The home page should also highlight Dr. Brennick' s qualification and provide a site map/navigation.

The colors of the logo do not need to be limited to black and white.  The logos MUST be integrated into the design, not just pasted on the page.

Read the brief carefully and pay careful attention to the target markets.

 

vector art uploaded:  logo.ai

Target Market(s)

OLDER men and women. People whose faces, eyes, etc., have an aged look that they want to look younger. ALSO patients who want to have the best possible vision after CATARACT SURGERY. Patients who want Premium IOL'S which give them vision at both distance and near WITHOUT GLASSES. STATE OF THE ART GLAUCOMA SURGERY.

Industry/Entity Type

Plastic

Requirements
Must have
• Easy to read. Some readers may have vision difficulties. Easy to navigate for the elderly market. Cosmetic page may be a little more complex.

```html
<!DOCTYPE html>
<html lang="en">
<head>
<meta charset="utf-8">
<title>Meridian Sightcare and Cosmetic Eyelid Surgery Center</title>
<link href="https://fonts.googleapis.com/css2?family=PT+Sans+Narrow:wght@400;700&family=Open+Sans:wght@400&family=Marcellus&display=swap" rel="stylesheet">
<style>
:root{
  --page-bg:#e6b992;
  --content-bg:#eefbc3;
  --about-bg:#e1f3f4;
  --nav-green:#8c9f54;
  --navy:#1a1d7c;
  --brand-blue:#1a22b8;
  --accent:#25b4e0;
  --mission:#6a6fb8;
  --rule:#c9d0a8;
  --button:#8fd9f2;
}
*{box-sizing:border-box;margin:0;padding:0}
html,body{width:1024px;height:1200px;overflow:hidden}
body{background:var(--page-bg);font-family:"PT Sans Narrow",sans-serif;color:var(--navy);position:relative}
.abs{position:absolute}
.column{left:80px;top:0;width:864px;height:1200px;background:var(--content-bg)}
.header{left:80px;top:0;width:864px;height:330px;background:linear-gradient(90deg,#d6e6f8,#c5e7f1 55%,#8fcfe0)}
.header-photo{left:210px;top:100px;width:400px;height:230px;background:linear-gradient(#e6d8cc,#cfd2da)}
.brand{left:120px;top:22px;display:flex;align-items:center;gap:12px;font-weight:700;font-size:36px;color:var(--brand-blue);line-height:1}
.brand-dot{width:32px;height:32px;border-radius:50%;background:var(--brand-blue)}
.center-title{left:600px;top:28px;width:280px;text-align:center;font-family:"Marcellus",serif;font-size:34px;line-height:36px;color:var(--brand-blue)}
.mission{left:622px;top:168px;width:292px;font-family:"Open Sans",sans-serif;color:var(--mission)}
.mission h2{font-weight:400;font-size:24px;margin-bottom:8px}
.mission p{font-size:14px;line-height:24.5px}
.nav{left:80px;top:330px;width:864px;height:48px;background:linear-gradient(#9db062,var(--nav-green) 60%,#7d9048);border-bottom:6px solid #c9cdb9}
.nav a{position:absolute;top:13px;transform:translateX(-50%);font-size:16px;font-weight:700;color:var(--navy);text-decoration:none;white-space:nowrap;text-shadow:0 1px 0 rgba(255,255,255,.4)}
.nav-tab{left:10px;top:3px;width:150px;height:39px;background:linear-gradient(#ffffff,#dfe1da);border-radius:14px 14px 0 0;clip-path:polygon(10% 0,100% 0,100% 100%,0 100%)}
h3.section{font-weight:400;font-size:18px;color:var(--accent);line-height:22px;text-transform:uppercase;white-space:nowrap}
h3.section.large{font-size:23px;line-height:24px}
h3.section em{font-style:normal;color:var(--navy)}
.copy{font-size:13.5px;line-height:20px}
.copy.small{font-size:12.5px;line-height:17px}
.btn{display:flex;align-items:center;justify-content:space-between;padding:0 8px;width:93px;height:28px;border-radius:5px;background:linear-gradient(#b3e8f8,var(--button));box-shadow:2px 3px 4px rgba(0,0,0,.25);font-family:"Open Sans",sans-serif;font-size:11.5px;color:#234;white-space:nowrap}
.btn svg{flex:none}
.frame{background:#fff;box-shadow:-8px 8px 8px rgba(0,0,0,.2)}
.rule{height:2px;background:var(--rule);border-bottom:1px solid #fff}
.care-list{list-style:none}
.care-list li{display:flex;align-items:center;gap:8px;height:30px;font-size:13px}
.bullet{width:16px;height:16px;border-radius:50%;background:radial-gradient(circle at 40% 35%,#d8f4fb,#4fb3d6);display:flex;align-items:center;justify-content:center}
.about{left:90px;top:934px;width:844px;height:216px;background:var(--about-bg)}
.contact-lines{font-size:12.5px;line-height:15px}
.footer{left:80px;top:1150px;width:864px;height:50px;background:var(--nav-green);color:#fff;text-align:center;font-size:11px;line-height:14px;padding-top:11px}
</style>
</head>
<body>
<div class="abs column"></div>

<header class="abs header"></header>
<div class="abs header-photo" role="img" aria-label="Photo of a smiling older couple looking at a laptop"></div>
<div class="abs brand"><span class="brand-dot"></span>Meridian Sightcare</div>
<div class="abs center-title">Cosmetic Eyelid<br>Surgery Center</div>
<div class="abs mission">
  <h2>Our mission:</h2>
  <p>To provide personal, friendly, state of the art general eye care as well as the latest advances in cosmetic eyelid surgery for men and women.</p>
</div>

<nav class="abs nav">
  <div class="abs nav-tab"></div>
  <a style="left:80px">Home</a>
  <a style="left:218px">General Eye Care</a>
  <a style="left:368px">Cosmetic Surgery</a>
  <a style="left:570px">About Dr. Martin Brennick</a>
  <a style="left:765px">Patients Potos</a>
</nav>

<section class="abs" style="left:117px;top:398px;width:378px">
  <h3 class="section large">Eyelid and Facial Cosmetic Surgery</h3>
  <p class="copy" style="margin-top:4px">Dr. Brennick specializes in cosmetic and reconstructive laser surgery of the eyelids and upper face. Because he performs the procedures with super-pulsed carbon dioxide lasers, his patients enjoy less bruising and swelling and are back to work (or play) sooner.</p>
  <p class="copy" style="margin-top:20px">Dr. Brennick is one of an elite rank of 400 surgeons nationally who are trained in the reconstruction and beautification of eyelids. Following his residency in Ophthalmology, Dr. Brennick was awarded a formal fellowship in eyelid plastic and orbital surgery (One of only 30 nationwide). Is cosmetic eyelid or facial plastic surgery right for you?</p>
  <p class="copy" style="margin-top:20px">Enter here to learn more about how cosmetic eyelid surgery can help you.</p>
</section>
<a class="abs btn" style="left:117px;top:669px">Read more <svg width="14" height="14"><circle cx="7" cy="7" r="7" fill="#555"/><path d="M5 4 L10 7 L5 10Z" fill="#fff"/></svg></a>

<div class="abs frame" style="left:512px;top:388px;width:393px;height:299px">
  <div role="img" aria-label="Close-up photo of an eye with long lashes" style="position:absolute;left:10px;top:9px;width:374px;height:280px;background:linear-gradient(160deg,#c9845a,#e8b08c 50%,#f0d2c0)"></div>
</div>

<div class="abs rule" style="left:117px;top:710px;width:788px"></div>

<section class="abs" style="left:117px;top:720px;width:170px">
  <h3 class="section">General Eyecare</h3>
  <ul class="care-list" style="margin-left:6px;margin-top:-3px">
    <li><span class="bullet"><svg width="8" height="8"><path d="M2 1 L7 4 L2 7Z" fill="#fff"/></svg></span>Cataract</li>
    <li><span class="bullet"><svg width="8" height="8"><path d="M2 1 L7 4 L2 7Z" fill="#fff"/></svg></span>Diabetic Retinopahy</li>
    <li><span class="bullet"><svg width="8" height="8"><path d="M2 1 L7 4 L2 7Z" fill="#fff"/></svg></span>Flashes and Floaters</li>
    <li><span class="bullet"><svg width="8" height="8"><path d="M2 1 L7 4 L2 7Z" fill="#fff"/></svg></span>Glaucoma</li>
    <li><span class="bullet"><svg width="8" height="8"><path d="M2 1 L7 4 L2 7Z" fill="#fff"/></svg></span>Macular Degeneration</li>
    <li><span class="bullet"><svg width="8" height="8"><path d="M2 1 L7 4 L2 7Z" fill="#fff"/></svg></span>Refractive Surgery</li>
  </ul>
</section>

<section class="abs" style="left:295px;top:721px;width:295px">
  <h3 class="section">Cosmetic Eyelid Surgery</h3>
  <p class="copy small" style="margin-top:1px">Our facial expression should mirror our emotional state, but other factors, some beyond our control, laso have an impact on our appearance. Heredity, over exposure to the sun, aging, and smoking, can all lead to slackening of the facial muscles and loosening of the facial skin.</p>
</section>
<a class="abs btn" style="left:295px;top:857px">Read more <svg width="14" height="14"><circle cx="7" cy="7" r="7" fill="#555"/><path d="M5 4 L10 7 L5 10Z" fill="#fff"/></svg></a>

<section class="abs" style="left:630px;top:720px;width:275px">
  <h3 class="section">Reconstructive Eyelid Surgery</h3>
  <p class="copy small" style="margin-top:2px">Our facial expression should mirror our emotional state, but other factors, some beyond our control, laso have an impact on our appearance. Heredity, over exposure to the sun, aging, andsmoking, can all lead to slackening of the facial muscles and loosening of the facial skin.</p>
</section>
<a class="abs btn" style="left:630px;top:857px">Read more <svg width="14" height="14"><circle cx="7" cy="7" r="7" fill="#555"/><path d="M5 4 L10 7 L5 10Z" fill="#fff"/></svg></a>

<div class="abs rule" style="left:117px;top:921px;width:788px"></div>

<div class="abs about"></div>
<div class="abs frame" style="left:108px;top:952px;width:139px;height:183px">
  <div role="img" aria-label="Portrait photo of the doctor in a suit" style="position:absolute;left:8px;top:8px;width:123px;height:167px;background:linear-gradient(#c79a6e,#8a6650 55%,#5a5a60)"></div>
</div>
<section class="abs" style="left:280px;top:942px;width:312px">
  <h3 class="section">About <em>Dr. Martin Brennick, M.D.</em></h3>
  <p class="copy small" style="margin-top:2px">Martin Brennick, M.D., a native of New York, has always been surrounded by art and artists. His interest in aesthetics is seen not only in his meticulous surgery, but also in his skill as a nature and landscape photographer. His professional education brought him westward.</p>
  <p class="copy small" style="margin-top:9px">After graduating Magna Cum Laude from Halden University, Boston, Massachusetts, he completed Medical School at Westbrook...</p>
</section>
<a class="abs btn" style="left:280px;top:1104px">Read more <svg width="14" height="14"><circle cx="7" cy="7" r="7" fill="#555"/><path d="M5 4 L10 7 L5 10Z" fill="#fff"/></svg></a>

<section class="abs" style="left:605px;top:942px;width:301px">
  <h3 class="section">Map to <em>Our Office</em></h3>
  <div role="img" aria-label="Street map showing the office location" style="margin-top:4px;width:301px;height:119px;border:1px solid #222;background:linear-gradient(135deg,#eef0e6,#e3e6d6 50%,#d8dccc)"></div>
</section>
<h3 class="abs section" style="left:605px;top:1095px">Contact Us</h3>
<div class="abs contact-lines" style="left:713px;top:1100px">217 HARBOR AVE. LINDALE, CA 95011<br>555-010-4821<br>Email: mbrennickmd@bright-lumen.com</div>

<footer class="abs footer">
  Home &nbsp;I&nbsp; Cosmetic Eyelid Surgery &nbsp;I&nbsp; Patiens Photos &nbsp;I&nbsp; About Dr. Martin Brennick &nbsp;I&nbsp; Map to our Office &nbsp;I&nbsp; Contac Us<br>
  @Copyright, 2011, www.bright-lumen.com &nbsp;I&nbsp; All Rights Resrved
</footer>
</body>
</html>
```